Tarrowind High School Association Website New Design

We require a fresh new website design for the Tarrowind High School Old Boys Association. The association is a non-for-profit and as such we like the site to reflect the ethos.
We require a design that uses responsive design techniques, so to allow the site to shift between mobile, tablet and desktop spaces and maintain elements in the site.
We would like a landing/home page design, and also an inner news/article based design included.
We want the site to appeal to a broad market of both the old guard members but also to bring on board the new social savey younger members.
The site needs to have a modern take on a professional yet fresh and opulent/elegant look.
A site that we like influences from is http://www.quennaval-lodge.com/ we especially like the navigation look and feel.
The site needs to be clean and simple to find information and navigate and as such would like the site design elements to reflect this in its layout and element interplay.
This site will act as an information gateway for the member's, but also offer abilities to purchase memberships, get information on up coming events and purchase tickets to these events, and interact with the members on the site.
Hi All designers,
The client has now agreed to make the project funding guaranteed, so I hope to see some great designs from you.
Thanks
Sorry all, I hadn't uploaded the logo, has now been uploaded.
Hi all designers, please don't let the wireframe layout include restrict your design freedom on the page layout. We included this to give you a feel for the elements wanted in the site, but not to push you to have them all in that arrangement. Feel free to move around or remove parts of to make better use of the space.
Also this site is for ex-students who are members of an association linked to the school, and not for the school itself, so your designs need to lean towards a member, events and reunions type site design.
After a review today, client now requires that the sites Events need special consideration. Want to see in a prominent position on the landing page area a good area to showcase the upcoming events. Please take this into consideration in your future design layouts.
Hi All Designers, I appreciate all the new and current designs, and sorry a bit behind on the feedback, have been a bit swamped on my own workload, I will give feedback to you all, and will maybe look at an extension of the deadline if need be, as to also allow the clients to look over designs.
Thanks
Reason: Extending the project deadline to allow more feedback to be provider to all designers, to allow review by clients and the feedback through myself.
Reason: Client was un-available for comment, and want them to be able to give feedback to designers for last round updates.
Reason: Sorry all, client has been overseas, and will only be back next week, so need to extend the deadline to allow for client input next week.
Reason: Sorry client has be delayed overseas, so when be needing to work through the designs next week to allow full ability to give all designs due recognition.
Reason: Waiting for client to review designs.
Target Market(s)
Professionals from all varity of job types
Industry/Entity Type
Events
Requirements
Must have
- Please use the attached Logo in the design and look to use the current colour pallet as much as possible, but open to colour and pallet additions or amendments.
Must have a “hero” header image scroller for ability to showcase upcoming events and other items (Required for home/landing pages, could be amended or removed on inner pages).
Should look to follow the include wire frame layout concept as a good conception starting point - but do not limit to just this layout, use design discretion.
Include prominently positioned events area in layout for upcoming events to push the events heavy aspect of the site.
Should include icons/link abilities to access social sites and applications. Ie Plumvine etc.
Nice to have
- A modern look with an edge to it.
Creative use of the sites colour pallet and site elements.
Should not have
- should not be a copy of the wireframe with colour added

```html
<!DOCTYPE html>
<html lang="en">
<head>
<meta charset="utf-8">
<title>Tarrowind High School Old Boys Association</title>
<link rel="stylesheet" href="https://fonts.googleapis.com/css2?family=Roboto+Condensed:wght@700&family=Arimo:wght@400;700&display=swap">
<style>
:root{
  --page:#f4efef;
  --header:#fdfcfc;
  --accent:#9b1a3d;
  --title:#7c6169;
  --text:#4a4345;
  --nav:#5b5557;
  --footer:#2a2728;
  --footer-text:#e6e2e2;
  --line:#e2d9da;
}
*{box-sizing:border-box;margin:0;padding:0}
html,body{width:1178px;height:1200px;overflow:hidden}
body{background:var(--page);font-family:"Arimo",Arial,sans-serif;color:var(--text);position:relative}
.site-header{position:absolute;left:0;top:0;width:1178px;height:109px;background:var(--header);border-bottom:1px solid var(--line)}
.brand{position:absolute;left:118px;top:42px;font-family:"Arimo",Arial,sans-serif;font-weight:700;font-size:26px;color:var(--accent);line-height:1}
.main-nav a{position:absolute;top:46px;font-size:17px;line-height:20px;color:var(--nav);text-decoration:none}
.main-nav a.is-active{top:39px;height:37px;width:89px;text-align:center;line-height:37px;background:var(--accent);color:#fff;border-radius:2px}
.search{position:absolute;left:880px;top:42px;width:180px;height:30px;border:1px solid var(--line);background:#fff;font-size:12px;color:#aaa;padding:8px 12px}
.search svg{position:absolute;right:9px;top:8px}
.page-title{position:absolute;left:0;top:134px;width:1178px;text-align:center;font-family:"Roboto Condensed",Arial,sans-serif;font-size:45px;line-height:54px;color:var(--title);letter-spacing:-0.5px}
.title-rule{position:absolute;top:161px;height:1px;background:#b9a9ad;width:108px}
.hero{position:absolute;left:118px;top:212px;width:942px;height:375px;background:#fff;padding:10px;box-shadow:0 18px 30px -12px rgba(80,50,60,.35)}
.hero-image{position:relative;width:100%;height:100%;background:linear-gradient(180deg,#5c6a55 0%,#4a4b3c 30%,#3a2f28 60%,#6a4a34 100%)}
.hero-caption{position:absolute;left:138px;top:302px;width:643px;height:30px;background:rgba(40,30,30,.55);color:#fff;font-size:13px;line-height:30px;text-align:center}
.hero-arrow{position:absolute;top:172px}
.dots{position:absolute;left:542px;top:624px;display:flex;gap:4px}
.dots span{width:9px;height:9px;border-radius:50%;background:#d8d0d2;border:1px solid #c8bcbf}
.dots span.is-active{background:var(--accent);border-color:var(--accent)}
.feature{position:absolute;top:666px;width:298px;height:214px;background:#fff;border:1px solid var(--line);box-shadow:0 2px 8px rgba(0,0,0,.08);padding:30px 22px 0 24px}
.feature.is-highlight{background:linear-gradient(180deg,#fdf6f8,#f3e3e8)}
.feature h2{font-size:21px;line-height:26px;font-weight:700;color:#333;display:flex;align-items:center;gap:9px;margin-bottom:12px}
.feature.is-highlight h2{color:var(--accent)}
.feature p{font-size:12px;line-height:18.5px;color:#444}
.read-more{display:inline-block;margin-top:12px;background:var(--accent);color:#fff;font-size:11px;padding:3px 8px}
.site-footer{position:absolute;left:118px;top:922px;width:942px;height:214px;background:var(--footer);color:var(--footer-text)}
.footer-col{position:absolute;top:40px}
.footer-col h3{font-size:19px;font-weight:700;color:#fff;margin-bottom:16px}
.footer-col li{list-style:none;font-size:12.5px;line-height:21px}
.footer-col .tag{display:inline-block;width:30px;color:#ccc}
.bullet{display:inline-block;width:14px;font-size:9px}
.sq{display:inline-block;width:10px;height:10px;margin-right:20px;vertical-align:-1px}
.newsletter{display:flex;margin-top:2px}
.newsletter span{width:152px;height:30px;background:#fff;color:#777;font-size:12px;line-height:30px;padding-left:10px}
.newsletter b{width:47px;height:30px;background:var(--accent);color:#fff;font-size:19px;line-height:30px;text-align:center}
.legal{position:absolute;top:1158px;font-size:12px;color:#666}
</style>
</head>
<body>
<header class="site-header">
  <div class="brand">Tarrowind OBA</div>
  <nav class="main-nav">
    <a href="#" style="left:352px">Home</a>
    <a href="#" style="left:429px">News</a>
    <a href="#" class="is-active" style="left:483px">Events</a>
    <a href="#" style="left:584px">Photos</a>
    <a href="#" style="left:668px">Membership</a>
    <a href="#" style="left:793px">Contact</a>
  </nav>
  <div class="search">Search
    <svg width="12" height="12" viewBox="0 0 12 12"><circle cx="5" cy="5" r="3.6" fill="none" stroke="#aaa" stroke-width="1.5"/><line x1="7.6" y1="7.6" x2="11" y2="11" stroke="#aaa" stroke-width="1.5"/></svg>
  </div>
</header>

<div class="title-rule" style="left:195px"></div>
<div class="title-rule" style="left:880px"></div>
<h1 class="page-title">The Association of Excellence</h1>

<section class="hero">
  <div class="hero-image" role="img" aria-label="Student jazz band performing with a conductor in a glass-roofed hall">
    <svg class="hero-arrow" style="left:28px" width="14" height="24" viewBox="0 0 14 24"><polyline points="12,2 2,12 12,22" fill="none" stroke="rgba(255,255,255,.6)" stroke-width="3"/></svg>
    <svg class="hero-arrow" style="right:28px" width="14" height="24" viewBox="0 0 14 24"><polyline points="2,2 12,12 2,22" fill="none" stroke="rgba(255,255,255,.6)" stroke-width="3"/></svg>
    <div class="hero-caption">behind the word mountains, far from the countries Vokalia and Consonantia, there live the blind texts.</div>
  </div>
</section>
<div class="dots"><span class="is-active"></span><span></span><span></span><span></span><span></span><span></span></div>

<article class="feature" style="left:118px">
  <h2><svg width="22" height="20" viewBox="0 0 22 20"><rect x="1" y="1" width="20" height="15" rx="2" fill="#333"/><circle cx="11" cy="7" r="3" fill="#fff"/><rect x="6" y="11" width="10" height="3" rx="1.5" fill="#fff"/></svg>Who We Are</h2>
  <p>Far far away, behind the word mountains, far from the countries Vokalia and Consonantia, there live the blind texts. Separated they live in Bookma rksgrove right at the coast of the Semantics, a large language ocean.</p>
  <span class="read-more">Read More &gt;</span>
</article>
<article class="feature is-highlight" style="left:439px">
  <h2><svg width="22" height="20" viewBox="0 0 22 20"><path d="M2 1h18v13H8l-5 5v-5H2z" fill="#9b1a3d"/><line x1="7" y1="10" x2="14" y2="4" stroke="#fff" stroke-width="2"/></svg>What We Do</h2>
  <p>Far far away, behind the word mountains, far from the countries Vokalia and Consonantia, there live the blind texts. Separated they live in Bookma rksgrove right at the coast of the Semantics, a large language ocean.</p>
  <span class="read-more">Read More &gt;</span>
</article>
<article class="feature" style="left:761px">
  <h2><svg width="22" height="20" viewBox="0 0 22 20"><path d="M2 1h18v13H8l-5 5v-5H2z" fill="#333"/><circle cx="8" cy="7.5" r="1.5" fill="#fff"/><circle cx="14" cy="7.5" r="1.5" fill="#fff"/></svg>How We Do It</h2>
  <p>Far far away, behind the word mountains, far from the countries Vokalia and Consonantia, there live the blind texts. Separated they live in Bookma rksgrove right at the coast of the Semantics, a large language ocean.</p>
  <span class="read-more">Read More &gt;</span>
</article>

<footer class="site-footer">
  <div class="footer-col" style="left:44px">
    <h3>Company</h3>
    <ul><li><span class="bullet">▸</span>Payments</li><li><span class="bullet">▸</span>About Us</li><li><span class="bullet">▸</span>Contact Us</li><li><span class="bullet">▸</span>More Links</li></ul>
  </div>
  <div class="footer-col" style="left:232px">
    <h3>Contact Us</h3>
    <ul><li><span class="tag">[P]</span>(03) 9400 5718</li><li><span class="tag">[E]</span>info@tarrowindoba.asn.au</li><li><span class="tag">[W]</span>www.tarrowindoba.asn.au</li><li><span class="tag">[P]</span>53 Tarrowind, Your Street</li><li><span class="tag"></span>to Go Here, Australia</li></ul>
  </div>
  <div class="footer-col" style="left:490px">
    <h3>Social Share</h3>
    <ul><li><span class="sq" style="background:#4a78b8"></span>Plumvine Fan</li><li><span class="sq" style="background:#e07a1f"></span>RSS Feeds</li><li><span class="sq" style="background:#3aa7d8"></span>Chirpline</li><li><span class="sq" style="background:#2a78a8"></span>Linkwell</li></ul>
  </div>
  <div class="footer-col" style="left:699px">
    <h3>Free Newsletter</h3>
    <div class="newsletter"><span>Enter your email</span><b>Join</b></div>
  </div>
</footer>
<p class="legal" style="left:118px">All Right Reserved Copyright © 2012 - www.tarrowindoba.asn.au</p>
<p class="legal" style="right:118px">Powered By : Loomfield Studio</p>
</body>
</html>
```